Kid's Cancer Camp Business Card

Create a unique Two-Sided color business cards for Camp Willow Brook, a pediatric cancer camp.

The camp tag line is: A place where kids with cancer have fun...

Dale Morrisey, Executive Director
Camp Willow Brook Charitable Foundation, Inc
PO Box 918
Ashgrove, CT 06832

Phone - 203-555-0143
Fax - 203-555-0187
Email: dale@campwillowbrook.example
www.campwillowbrook.example

Target Market(s)

Potential Donors, Volunteers and Campers

Industry/Entity Type

Non-profit pediatric cancer camp

Contact Information for Business Card

All contact info that is included in the description

Font styles to use
Other font styles liked:
• Designer chooses font

Requirements
Must have
• Camp Willow Brook Logo and Tag Line
Nice to have
• should be eye catching
Should not have
• not cartoony

```html
<!DOCTYPE html>
<html lang="en">
<head>
<meta charset="utf-8">
<title>Camp Willow Brook – Business Card</title>
<link rel="stylesheet" href="https://fonts.googleapis.com/css2?family=Roboto:wght@400;500;700&family=Roboto+Condensed:wght@700&display=swap">
<style>
  :root{
    --bg:#e4e4e4;
    --card-white:#ffffff;
    --camp-blue:#0d67a0;
    --camp-blue-deep:#0a5686;
    --camp-blue-light:#2f8cc4;
    --camp-teal:#13a08c;
    --sun-orange:#f8b225;
    --text-grey:#5a5a5a;
  }
  *{box-sizing:border-box;margin:0;padding:0}
  html,body{width:1200px;height:801px;overflow:hidden;background:var(--bg)}
  body{font-family:"Roboto",Arial,sans-serif;position:relative}

  .card{
    position:absolute;width:520px;height:297px;top:252px;
    box-shadow:0 6px 18px rgba(0,0,0,.18);overflow:hidden;
  }
  .card--front{left:60px;background:var(--card-white);border-bottom:4px solid var(--camp-blue)}
  .card--back{left:620px;background:var(--camp-blue)}

  /* front */
  .brand{position:absolute;top:44px;right:40px;display:flex;align-items:center;gap:10px}
  .brand__dot{width:22px;height:22px;border-radius:50%;background:var(--sun-orange)}
  .brand__name{font-size:24px;font-weight:500;color:var(--camp-blue)}

  .divider{position:absolute;left:30px;right:30px;top:150px;height:1px;background:var(--camp-blue)}

  .person{position:absolute;left:30px;top:98px}
  .person__name{font-family:"Roboto Condensed",Arial,sans-serif;font-weight:700;font-size:22px;color:var(--camp-blue);letter-spacing:.5px;text-transform:uppercase;line-height:1.1}
  .person__title{font-size:15px;color:var(--camp-teal);margin-top:3px}

  .contact{position:absolute;left:30px;top:166px;list-style:none}
  .contact li{display:flex;align-items:center;gap:9px;font-size:13.5px;color:var(--text-grey);line-height:19px}
  .contact svg{width:12px;height:12px;flex:none;fill:var(--sun-orange)}

  .address{position:absolute;right:30px;top:166px;text-align:right;font-size:13.5px;color:var(--text-grey);line-height:19px;font-style:normal}

  /* back */
  .pattern{position:absolute;inset:0;background:linear-gradient(160deg,var(--camp-blue-deep) 0%,var(--camp-blue) 50%,var(--camp-blue-light) 100%)}
  .back-brand{position:absolute;right:44px;top:118px;display:flex;align-items:center;gap:8px}
  .back-brand__dot{width:18px;height:18px;border-radius:50%;background:var(--sun-orange)}
  .back-brand__name{font-size:17px;font-weight:500;color:var(--card-white)}
  .tagline{position:absolute;left:44px;bottom:58px;font-family:"Roboto Condensed",Arial,sans-serif;font-weight:700;font-size:17px;letter-spacing:1px;color:var(--card-white);text-transform:uppercase;line-height:1.35}
</style>
</head>
<body>

<section class="card card--front" aria-label="Business card front">
  <div class="brand">
    <span class="brand__dot"></span>
    <span class="brand__name">Camp Willow Brook</span>
  </div>

  <div class="person">
    <p class="person__name">Dale Morrisey</p>
    <p class="person__title">Executive Director</p>
  </div>

  <div class="divider"></div>

  <ul class="contact">
    <li><svg viewBox="0 0 12 12"><path d="M2.5 0.5l2 2.2-1 1.3c.6 1.5 1.9 2.8 3.5 3.5l1.3-1 2.2 2-1.2 2.2C5 10.2 1.8 7 .3 1.7z"/></svg>203-555-0143</li>
    <li><svg viewBox="0 0 12 12"><rect x="3" y="0.5" width="6" height="3"/><rect x="0.5" y="4" width="11" height="5" rx="1"/><rect x="3" y="8" width="6" height="3.5"/></svg>203-555-0187</li>
    <li><svg viewBox="0 0 12 12"><path d="M0.5 2h11v8h-11z M1.2 2.6L6 6.6l4.8-4"/></svg>dale@campwillowbrook.example</li>
    <li><svg viewBox="0 0 12 12"><circle cx="6" cy="6" r="5.5"/></svg>www.campwillowbrook.example</li>
  </ul>

  <address class="address">
    Camp Willow Brook Charitable Foundation, Inc<br>
    PO Box 918<br>
    Ashgrove, CT 06832
  </address>
</section>

<section class="card card--back" aria-label="Business card back">
  <div class="pattern" role="img" aria-label="Repeating embossed sun-and-wave pattern in shades of blue"></div>
  <div class="back-brand">
    <span class="back-brand__dot"></span>
    <span class="back-brand__name">Camp Willow Brook</span>
  </div>
  <p class="tagline">A place where kids<br>with cancer have fun...</p>
</section>

</body>
</html>
```